Could You Go Solo Tomorrow? Podcast

We need a "Podcast Cover" for inclusion on Tunora and wavepocket along with a matching or complimentary banner to be included on a landing page which will be hosted on Castlyn (a Castlyn template). The Podcast is called the "Could You Go Solo Tomorrow?" Podcast and has a tag line of "Hear it before you jump".

I've included an image for a bit of inspiration that shows a person ready to leap into the unknown which, in our podcast, is like a metaphor for launching a business. You may use the photo in your design if you wish or do something completely different including "cartoon" characters or simply text.

Target Market(s)

People who are thinking about starting a new business or buying an existing business and whom have never owned a business before.

Industry/Entity Type

Startup

Font styles to use
Sans Serif

Colors

Designer to choose colors to be used in the design.

Requirements
Must have
• incorporate the "Hear it before you jump" tagline.

```html
<!DOCTYPE html>
<html lang="en">
<head>
<meta charset="utf-8">
<title>Could You Go Solo Tomorrow? Podcast Cover</title>
<link rel="stylesheet" href="https://fonts.googleapis.com/css2?family=Montserrat:wght@800&family=Open+Sans:wght@300&display=swap">
<style>
  :root {
    --sky-blue: #7f93b8;
    --sunset-orange: #e8743a;
    --sunset-glow: #f6b060;
    --city-dark: #2b2126;
    --city-mid: #5a3e3c;
    --title-white: #ffffff;
    --band-dark: rgba(36, 30, 38, 0.88);
    --tagline-grey: #d8d6da;
  }
  html, body {
    margin: 0;
    padding: 0;
    overflow: hidden;
    background: #000;
  }
  .cover {
    position: relative;
    width: 1200px;
    height: 1200px;
    overflow: hidden;
  }
  .cover__scene {
    position: absolute;
    inset: 0;
    background:
      radial-gradient(ellipse 30% 18% at 58% 25%, var(--sunset-glow) 0%, rgba(246,176,96,0) 100%),
      linear-gradient(180deg, var(--sky-blue) 0%, #c98a7a 12%, var(--sunset-orange) 24%, var(--city-mid) 42%, #3d2d30 65%, var(--city-dark) 100%);
  }
  .cover__title {
    position: absolute;
    left: 0;
    right: 0;
    top: 300px;
    margin: 0;
    text-align: center;
    color: var(--title-white);
    text-shadow: 0 2px 10px rgba(0, 0, 0, 0.35);
    font-family: "Montserrat", sans-serif;
    font-weight: 800;
    letter-spacing: -2px;
  }
  .title__line {
    display: block;
    font-size: 124px;
    line-height: 138px;
  }
  .cover__tagline {
    position: absolute;
    left: 0;
    top: 756px;
    width: 1064px;
    height: 80px;
    margin: 0;
    padding-left: 120px;
    box-sizing: border-box;
    background: var(--band-dark);
    color: var(--tagline-grey);
    font-family: "Open Sans", sans-serif;
    font-weight: 300;
    font-size: 50px;
    line-height: 80px;
    text-align: center;
  }
</style>
</head>
<body>
  <main class="cover">
    <div class="cover__scene" role="img" aria-label="Photo: a person seen from behind leading the viewer by the hand to the edge of a rooftop above a city skyline at sunset"></div>
    <h1 class="cover__title">
      <span class="title__line">COULD YOU</span>
      <span class="title__line">GO SOLO</span>
      <span class="title__line">TOMORROW?</span>
    </h1>
    <p class="cover__tagline">HEAR IT BEFORE YOU JUMP</p>
  </main>
</body>
</html>
```